Business Card Design Project

Hello Designers, hope you are all aiming enjoy the weekend
I have the Business Logo (uploaded), you can alter the color which ever way you think would work,
Im looking for a simple yet striking feel, something which will stay memorable (I have uploaded 3 examples for you to flick through)
Information on the card, will just be the bare minimum,
Double Sided
Info being
i.e.
Name
Number
Website
ABN
Tobin Wexmoor
+468213579 (singapore)
+315792846 (Australia)
+729384615 (America)
www.lomevu-linkup.example
ABN 86420913
Enjoy,
Tobin
Industry/Entity Type
Business
Look and feel
Each slider illustrates characteristics of the customer's brand and the style your logo design should communicate.

```html
<!DOCTYPE html>
<html lang="en">
<head>
<meta charset="utf-8">
<title>Lomevu Linkup – Business Cards</title>
<link rel="stylesheet" href="https://fonts.googleapis.com/css2?family=Ubuntu:wght@400;500&display=swap">
<style>
  :root {
    --backdrop: #2b2b2b;
    --card-light: #f4f4f4;
    --card-mid: #dcdcdc;
    --card-edge: #cfcfcf;
    --brand-red: #b5213c;
    --ink-grey: #5c5c5c;
    --ink-dark: #3a3a3a;
    --white: #ffffff;
  }
  * { box-sizing: border-box; margin: 0; padding: 0; }
  html, body {
    width: 1200px; height: 900px; overflow: hidden;
    background: var(--backdrop);
    font-family: "Ubuntu", sans-serif;
  }
  .stage {
    position: relative; width: 1200px; height: 900px;
  }
  .card {
    position: absolute; top: 80px;
    width: 400px; height: 740px;
    border-radius: 14px; overflow: hidden;
    background:
      radial-gradient(ellipse 120% 60% at 70% 45%, var(--card-light) 0%, rgba(244,244,244,0) 70%),
      linear-gradient(180deg, var(--card-mid) 0%, var(--card-light) 45%, var(--card-mid) 100%);
    border: 1px solid var(--card-edge);
  }
  .card--front { left: 180px; }
  .card--back { left: 620px; }

  .card__wash {
    position: absolute; inset: 0;
  }

  .brand-mark {
    position: absolute; left: 0; right: 0;
    display: flex; flex-direction: column; align-items: center;
  }
  .card--front .brand-mark { top: 210px; }
  .brand-mark__square {
    width: 54px; height: 54px; border-radius: 8px;
    background: var(--brand-red);
  }
  .brand-mark__name {
    margin-top: 24px;
    font-weight: 500; font-size: 50px; letter-spacing: -0.5px;
    color: var(--ink-grey); white-space: nowrap;
  }

  .name-band {
    position: absolute; top: 322px; left: 0; right: 0; height: 40px;
    background: var(--brand-red);
    color: var(--white);
    font-size: 27px; font-weight: 400;
    display: flex; align-items: center; justify-content: center;
  }

  .contact {
    position: absolute; left: 26px; top: 378px;
    list-style: none; font-size: 11.5px; color: var(--ink-dark);
  }
  .contact li {
    display: flex; align-items: center; gap: 8px; height: 18px;
  }
  .contact svg { width: 12px; height: 12px; flex: none; }
  .contact .contact__web { margin-top: 20px; }
  .contact .contact__abn { margin-top: 14px; padding-left: 20px; }

  .card--back .brand-mark {
    top: 680px; flex-direction: row; gap: 12px;
  }
  .card--back .brand-mark__square { width: 34px; height: 34px; border-radius: 6px; }
  .card--back .brand-mark__name { margin-top: 0; font-size: 32px; }
</style>
</head>
<body>
<main class="stage">
  <section class="card card--front" aria-label="Card front">
    <div class="card__wash" role="img" aria-label="Soft grey curved light wash"></div>
    <div class="brand-mark">
      <div class="brand-mark__square"></div>
      <div class="brand-mark__name">Lomevu Linkup</div>
    </div>
  </section>

  <section class="card card--back" aria-label="Card back">
    <div class="card__wash" role="img" aria-label="Soft grey curved light wash"></div>
    <div class="name-band">Tobin Wexmoor</div>
    <ul class="contact">
      <li>
        <svg viewBox="0 0 12 12" aria-hidden="true"><rect width="12" height="12" rx="2" fill="#b5213c"/><path d="M3 4.5c0-1 1-1.5 3-1.5s3 .5 3 1.5v.8H7.6V4.6H4.4v.7H3zM3.5 6h5l.5 3H3z" fill="#fff"/></svg>
        +468213579 (Singapore)
      </li>
      <li>
        <svg viewBox="0 0 12 12" aria-hidden="true"><rect width="12" height="12" rx="2" fill="#b5213c"/><path d="M3 4.5c0-1 1-1.5 3-1.5s3 .5 3 1.5v.8H7.6V4.6H4.4v.7H3zM3.5 6h5l.5 3H3z" fill="#fff"/></svg>
        +315792846 (Australia)
      </li>
      <li>
        <svg viewBox="0 0 12 12" aria-hidden="true"><rect width="12" height="12" rx="2" fill="#b5213c"/><path d="M3 4.5c0-1 1-1.5 3-1.5s3 .5 3 1.5v.8H7.6V4.6H4.4v.7H3zM3.5 6h5l.5 3H3z" fill="#fff"/></svg>
        +729384615 (America)
      </li>
      <li class="contact__web">
        <svg viewBox="0 0 12 12" aria-hidden="true"><circle cx="6" cy="6" r="5.3" fill="none" stroke="#b5213c" stroke-width="1.2"/><ellipse cx="6" cy="6" rx="2.2" ry="5.3" fill="none" stroke="#b5213c" stroke-width="1"/><path d="M.8 6h10.4" stroke="#b5213c" stroke-width="1"/></svg>
        www.lomevu-linkup.example
      </li>
      <li class="contact__abn">ABN 86420913</li>
    </ul>
    <div class="brand-mark">
      <div class="brand-mark__square"></div>
      <div class="brand-mark__name">Lomevu Linkup</div>
    </div>
  </section>
</main>
</body>
</html>
```